Business Card Design for ClearPathVitality

We need the new logo on a business card for 3 employees:
Nora Kettering, PhD, Advanced Instructor and Practitioner of SomaLink Integral Medicine (email: nora@clearpathvitality.com)
Ray Holm, Business Manager (email: ray@clearpathvitality.com)
Bea Marlowe, Administrative Assistant (email: bea@helixsense.com)

Target Market(s)

healthcare professionals

Industry/Entity Type

Alternative Medicine

Contact Information for Business Card

Names, titles, emails (names, titles, emails are in project description), phone, address, website, with logo and tagline. See below for address, phone, website: 418 Alder Ln, Bldg 12, Ste 305
Santa Cruz, CA 95060
831-555-2746
www.clearpathvitality.com
Tagline: Roots of Balance, Light of Renewal

Font styles to use
Other font styles liked:
• Gabriela

Colors
00a990
86cfc6
6b449b
b7a5cd
85abd2
abd036

Requirements
Must have
• Colors and style that match the logo design - shades such as blue, green, purple
• Compatible or same font as in the logo
Nice to have
• Nice if it goes with the theme of Nora's last business card - uploaded below
Should not have
• colors or style in conflict with the logo

```html
<!DOCTYPE html>
<html lang="en">
<head>
<meta charset="utf-8">
<title>ClearPathVitality Business Card</title>
<link rel="stylesheet" href="https://fonts.googleapis.com/css2?family=Gabriela&family=Barlow:wght@400;500;600&display=swap">
<style>
  :root {
    --stage: #3b3b3d;
    --card-blue-top: #2a64ad;
    --card-blue-bottom: #134a94;
    --white: #ffffff;
    --ink: #1d1d1f;
    --navy: #1f3f86;
    --purple: #4a2a7a;
    --green: #3fb34a;
    --teal: #00a990;
    --lilac-faint: #eeeaf4;
    --mint-faint: #eef7ea;
  }
  * { box-sizing: border-box; margin: 0; padding: 0; }
  html, body { width: 1200px; height: 1000px; overflow: hidden; }
  body { background: var(--stage); position: relative; font-family: "Barlow", sans-serif; }

  .card {
    position: absolute;
    width: 700px;
    height: 400px;
    border-radius: 22px;
    overflow: hidden;
  }

  /* Front */
  .card-front {
    left: 400px; top: 60px;
    background: linear-gradient(180deg, var(--card-blue-top), var(--card-blue-bottom));
  }
  .front-texture {
    position: absolute; inset: 0;
    background: radial-gradient(ellipse at 80% 40%, rgba(255,255,255,0.08), rgba(255,255,255,0) 60%);
  }
  .front-brand {
    position: absolute; left: 130px; top: 100px;
    display: flex; align-items: center; gap: 22px;
  }
  .brand-dot {
    width: 120px; height: 120px; border-radius: 50%;
    background: var(--teal);
    flex: none;
  }
  .front-brand .brand-name {
    font-family: "Gabriela", serif;
    font-size: 40px;
    color: var(--white);
  }
  .tagline {
    position: absolute; left: 0; right: 0; top: 300px;
    text-align: center;
    font-family: "Gabriela", serif;
    font-size: 17px;
    letter-spacing: 1px;
    text-transform: uppercase;
    color: var(--white);
  }

  /* Back */
  .card-back {
    left: 100px; top: 530px;
    background: var(--white);
  }
  .back-halo {
    position: absolute; left: 470px; top: 150px;
    width: 420px; height: 420px; border-radius: 50%;
    background: var(--lilac-faint);
    opacity: 0.8;
  }
  .back-brand {
    position: absolute; left: 36px; top: 36px;
    display: flex; align-items: center; gap: 16px;
  }
  .back-brand .brand-dot { width: 96px; height: 96px; }
  .back-brand .brand-name {
    font-family: "Gabriela", serif;
    font-size: 32px;
    color: var(--purple);
  }
  .contact {
    position: absolute; left: 40px; top: 238px;
    font-size: 15px; line-height: 1.45; color: var(--ink);
  }
  .contact-line { display: flex; align-items: center; gap: 6px; }
  .contact-line svg { width: 13px; height: 13px; flex: none; }
  .address { margin-bottom: 6px; }

  .person {
    position: absolute; right: 40px; top: 258px; text-align: right;
  }
  .person-name {
    font-family: "Gabriela", serif;
    font-size: 24px; color: var(--navy);
  }
  .person-title {
    font-family: "Gabriela", serif;
    font-size: 11px; text-transform: uppercase; color: var(--ink);
    margin-top: 2px;
  }
  .accent-bar {
    position: absolute; right: 0; top: 258px;
    width: 28px; height: 34px; background: var(--green);
  }
  .website {
    position: absolute; right: 40px; bottom: 30px;
    font-size: 17px; font-weight: 500; color: var(--ink);
  }
  .website .domain { color: var(--navy); font-weight: 600; }
</style>
</head>
<body>

<section class="card card-front" aria-label="Card front">
  <div class="front-texture" role="img" aria-label="Faint helix pattern across the blue background"></div>
  <div class="front-brand">
    <span class="brand-dot"></span>
    <span class="brand-name">ClearPathVitality</span>
  </div>
  <p class="tagline">Roots of Balance, Light of Renewal</p>
</section>

<section class="card card-back" aria-label="Card back">
  <div class="back-halo"></div>
  <div class="back-brand">
    <span class="brand-dot"></span>
    <span class="brand-name">ClearPathVitality</span>
  </div>

  <div class="contact">
    <p class="address">418 Alder Ln, Bldg 12,<br>Ste 305 Santa Cruz, CA 95060</p>
    <p class="contact-line">
      <svg viewBox="0 0 16 16" aria-hidden="true"><path fill="#3fb34a" d="M3.6 1.5l2.3 2.6-1.3 1.8c.9 2 2.5 3.6 4.5 4.5l1.8-1.3 2.6 2.3-1.2 2.4C7 13.3 2.7 9 1.2 2.7z"/></svg>
      831-555-2746
    </p>
    <p class="contact-line">
      <svg viewBox="0 0 16 16" aria-hidden="true"><rect x="1" y="3" width="14" height="10" rx="1.5" fill="#3fb34a"/><path d="M2 4.5l6 4.5 6-4.5" fill="none" stroke="#fff" stroke-width="1.3"/></svg>
      nora@clearpathvitality.com
    </p>
  </div>

  <div class="person">
    <p class="person-name">Nora Kettering</p>
    <p class="person-title">PhD, Advanced Instructor and Practitioner</p>
  </div>
  <div class="accent-bar"></div>

  <p class="website">www.<span class="domain">clearpathvitality</span>.com</p>
</section>

</body>
</html>
```